VALMIRA/ VALMIRA GREY Business Card

We have two brands that we would like to show one 1 business card (front and back). We would to incorporate two different logos on one card (VALMIRA and VALMIRA GREY). Card can be two sided. Simple, sleek and professional.

We are a senior living provider.

www.valmira-example.com
www.valmiragrey-example.com

Target Market(s)

Professionals

Industry/Entity Type

Business

Font styles to use
Serif

Colors

Designer to choose colors to be used in the design.

Requirements
Must have
• Space for EMAIL, PHONE, WEBSITE
Nice to have
• Raised lettering or gloss lettering

```html
<!DOCTYPE html>
<html lang="en">
<head>
<meta charset="utf-8">
<title>VALMIRA / VALMIRA GREY Business Cards</title>
<link rel="stylesheet" href="https://fonts.googleapis.com/css2?family=Cinzel:wght@400;500&family=PT+Sans:wght@400&display=swap">
<style>
  :root {
    --page: #ffffff;
    --page-edge: #4a4a4a;
    --card-dark: #1c1b1a;
    --card-mid: #2c2a27;
    --card-light: #3a3733;
    --gold: #8c6b3b;
    --gold-line: #7a5d33;
    --silver: #c9c9c7;
    --footer-text: #a9a7a3;
  }
  * { margin: 0; padding: 0; box-sizing: border-box; }
  html, body {
    width: 1200px;
    height: 1200px;
    overflow: hidden;
    background: var(--page);
  }
  .canvas {
    position: relative;
    width: 1200px;
    height: 1200px;
    border: 1px solid var(--page-edge);
    background: var(--page);
  }
  .card {
    position: absolute;
    border-radius: 7px;
    overflow: hidden;
    background: var(--card-dark);
  }
  .card--front { left: 258px; top: 135px; width: 685px; height: 421px; }
  .card--back  { left: 261px; top: 639px; width: 681px; height: 424px; }

  .card__photo {
    position: absolute;
    inset: 0;
  }
  .card--front .card__photo {
    background:
      linear-gradient(90deg, rgba(0,0,0,0) 55%, rgba(70,66,60,0.35) 62%, rgba(0,0,0,0) 70%),
      linear-gradient(180deg, var(--card-mid) 0%, var(--card-dark) 55%, var(--card-mid) 100%);
  }
  .card--back .card__photo {
    background:
      linear-gradient(160deg, var(--card-light) 0%, var(--card-mid) 35%, var(--card-dark) 75%, var(--card-mid) 100%);
  }

  .brand {
    position: absolute;
    display: flex;
    align-items: center;
  }
  .brand__mark {
    flex: none;
    background: var(--gold);
  }
  .brand__name {
    font-family: "Cinzel", serif;
    font-weight: 400;
    line-height: 1;
    white-space: nowrap;
  }

  .card--front .brand {
    left: 0; right: 0; top: 105px;
    justify-content: center;
    gap: 28px;
  }
  .card--front .brand__mark { width: 92px; height: 92px; }
  .card--front .brand__name { font-size: 86px; color: var(--gold); letter-spacing: 1px; }

  .card--back .brand {
    left: 40px; top: 166px;
    gap: 26px;
  }
  .card--back .brand__mark { width: 88px; height: 88px; background: var(--silver); }
  .brand__text { display: flex; flex-direction: column; gap: 10px; }
  .card--back .brand__name { font-size: 46px; color: var(--silver); letter-spacing: 1px; }
  .brand__tagline {
    font-family: "PT Sans", sans-serif;
    font-size: 27px;
    color: var(--silver);
    white-space: nowrap;
  }

  .contact {
    position: absolute;
    left: 40px; right: 38px;
    display: flex;
    justify-content: space-between;
    padding-top: 7px;
    border-top: 1px solid var(--gold-line);
    font-family: "PT Sans", sans-serif;
    font-size: 15px;
    color: var(--footer-text);
  }
  .card--front .contact { top: 367px; }
  .card--back .contact { top: 369px; }
</style>
</head>
<body>
<main class="canvas">

  <section class="card card--front" aria-label="Card front, VALMIRA">
    <div class="card__photo" role="img" aria-label="Dark, dim photograph of a modern building interior"></div>
    <div class="brand">
      <span class="brand__mark"></span>
      <span class="brand__name">VALMIRA</span>
    </div>
    <div class="contact">
      <span>www.valmira-example.com</span>
      <span>info@valmira-example.com</span>
      <span>011 555 0187</span>
    </div>
  </section>

  <section class="card card--back" aria-label="Card back, VALMIRA GREY">
    <div class="card__photo" role="img" aria-label="Dark, dim photograph of a glass and steel building facade"></div>
    <div class="brand">
      <span class="brand__mark"></span>
      <div class="brand__text">
        <span class="brand__name">VALMIRA GREY</span>
        <span class="brand__tagline">Executive Personal Care Services</span>
      </div>
    </div>
    <div class="contact">
      <span>www.valmiragrey-example.com</span>
      <span>info@valmiragrey-example.com</span>
      <span>011 555 0198</span>
    </div>
  </section>

</main>
</body>
</html>
```